Construction Directory Website Flyer

We need a postcard size +/- or somewhere around that size (something standard) flyer designed for our construction directory website. Leave a spot for tagline. Call to action is 'register your company now'. I am thinking many mini pictures of different construction to show that it is for the entire construction industry. Logo and screenshot of the homepage of the website is attached. Use same theme as webpage.

Target Market(s)

Construction Industry

Industry/Entity Type

Construction

Font styles to use
Sans Serif

Requirements
Must have
• Call to action
• Colors to match logo
• Area to add description and details.
Nice to have
• Construction Images
Should not have
• No Cartoonish types of things

```html
<!DOCTYPE html>
<html lang="en">
<head>
<meta charset="UTF-8">
<title>Buildwise Network Flyer</title>
<link href="https://fonts.googleapis.com/css2?family=Jost:wght@400;500;700;800&display=swap" rel="stylesheet">
<style>
  :root {
    --stage: #e6e6e6;
    --paper: #f1f1f3;
    --paper-shade: #e4e4e8;
    --ink: #4a4f57;
    --body-ink: #3c3f44;
    --white: #ffffff;
    --accent: #e8431c;
    --sky: #dfe4ea;
    --gold: #b9803f;
    --brick: #6b4a36;
    --shadow: #1c1a1a;
  }
  * { margin: 0; padding: 0; box-sizing: border-box; }
  html, body {
    width: 1200px; height: 1200px; overflow: hidden;
    background: var(--stage);
    font-family: "Jost", sans-serif;
  }
  .flyer {
    position: absolute; left: 272px; top: 108px;
    width: 656px; height: 984px;
    background: linear-gradient(160deg, var(--paper) 0%, var(--paper-shade) 100%);
    overflow: hidden;
  }
  .hero-photo {
    position: absolute; left: 0; top: 0; width: 656px; height: 744px;
    background:
      radial-gradient(ellipse 160px 220px at 150px 360px, rgba(255,196,90,0.75), rgba(255,196,90,0) 70%),
      linear-gradient(180deg, var(--sky) 0%, #d9d8d6 22%, #a89684 38%, var(--gold) 50%, var(--brick) 66%, #3a2e29 82%, var(--shadow) 100%);
  }
  .brand {
    position: absolute; left: 54px; top: 70px;
    display: flex; align-items: center; gap: 14px;
  }
  .brand-mark { width: 44px; height: 44px; background: var(--accent); }
  .brand-name {
    font-weight: 500; font-size: 28px; line-height: 1; color: var(--ink);
    letter-spacing: 0.2px;
  }
  .headline-marker {
    position: absolute; left: 0; top: 544px; width: 26px; height: 56px;
  }
  .headline {
    position: absolute; left: 54px; top: 522px;
    font-weight: 700; font-size: 40px; line-height: 50px;
    color: var(--white); letter-spacing: 0.4px; text-transform: uppercase;
  }
  .cta {
    position: absolute; left: 338px; top: 662px; width: 263px; height: 164px;
    background: var(--accent); color: var(--white); text-align: center;
    padding-top: 30px;
  }
  .cta::after {
    content: ""; position: absolute; inset: 11px;
    border: 1px solid rgba(255,255,255,0.55);
  }
  .cta-line { font-weight: 400; font-size: 26px; line-height: 31px; }
  .cta-phone { font-weight: 700; font-size: 30px; line-height: 36px; margin-top: 2px; }
  .details {
    position: absolute; font-size: 10px; line-height: 18.4px;
    color: var(--body-ink); text-align: justify;
  }
  .details-main { left: 53px; top: 786px; width: 264px; }
  .details-side { left: 338px; top: 842px; width: 264px; }
</style>
</head>
<body>
  <div class="flyer">
    <div class="hero-photo" role="img" aria-label="Photograph of a dense city skyline of high-rise towers at sunset, golden light along a street"></div>

    <div class="brand">
      <span class="brand-mark"></span>
      <span class="brand-name">Buildwise Network</span>
    </div>

    <svg class="headline-marker" viewBox="0 0 26 56" aria-hidden="true">
      <polygon points="0,0 26,28 0,56" fill="#e8431c"/>
    </svg>
    <h1 class="headline">Built by construction<br>for construction</h1>

    <div class="cta">
      <div class="cta-line">REGISTER YOUR</div>
      <div class="cta-line">COMPANY NOW</div>
      <div class="cta-phone">012-555-0147</div>
    </div>

    <p class="details details-main">Lorem ipsum dolor sit amet, consectetuer adipiscing elit, sed diam nonummy nibh euismod tincidunt ut laoreet dolore magna aliquam erat volutpat. Ut wisi enim ad minim veniam, quis nostrud exerci tation ullamcorper suscipit lobortis nisl ut aliquip ex ea commodo consequat. Duis autem vel eum iriure dolor in hendrerit in vulputate velit esse molestie consequat, vel illum dolore eu feugiat nulla facilisis</p>

    <p class="details details-side">Lorem ipsum dolor sit amet, consectetuer adipiscing elit, sed diam nonummy nibh euismod tincidunt ut laoreet dolore magna aliquam erat volutpat. Ut wisi enim ad minim veniam, quis nostrud.</p>
  </div>
</body>
</html>
```